Bref créative
Corvane Oral Care Stationary
Corvane Oral Care
Professional
R. Lucien Dorvash, DDS, MAGD
2483 W Perrin Ave.
Baytown, TX 77520
dentist@qbl.zx.com
www.corvaneoralcare.com

```html
<!DOCTYPE html>
<html lang="en">
<head>
<meta charset="utf-8">
<title>Corvane Oral Care Stationery</title>
<link href="https://fonts.googleapis.com/css2?family=Open+Sans:wght@400;700&display=swap" rel="stylesheet">
<style>
:root{
  --navy:#2c4a8f;
  --green:#8cc63f;
  --teal:#5fa8a0;
  --ink:#3a3a3a;
  --muted:#7a7a7a;
  --paper:#ffffff;
  --silver:#d9dadc;
  --backdrop:#ecebe8;
  --faint:#e4ebf3;
}
*{box-sizing:border-box;margin:0;padding:0}
html,body{width:1200px;height:497px;overflow:hidden}
body{background:var(--backdrop);font-family:"Open Sans",sans-serif;color:var(--ink);position:relative}
.card,.letterhead,.envelope{position:absolute;background:var(--paper);box-shadow:0 2px 6px rgba(0,0,0,.18);overflow:hidden}
.card{width:192px;height:108px;border-radius:6px}
.card--green{background:radial-gradient(ellipse at center,#ffffff 0%,#d9ecc2 45%,var(--green) 75%,var(--navy) 110%)}
.card--silver{background:radial-gradient(ellipse at center,#ffffff 0%,var(--silver) 90%)}
.brand{font-weight:700;color:var(--navy);line-height:1.1;text-align:center;display:flex;align-items:center;gap:5px}
.brand__dot{width:10px;height:10px;border-radius:50%;background:var(--green);flex:none}
.brand--small{font-size:8px}
.brand--center{position:absolute;left:50%;top:50%;transform:translate(-50%,-50%);font-size:12px;white-space:nowrap}
.mark{position:absolute;left:50%;top:50%;width:46px;height:46px;border-radius:50%;background:var(--navy);transform:translate(-50%,-50%);opacity:.85}
.card__brand{position:absolute;left:12px;top:14px;width:70px}
.card__name{position:absolute;left:96px;top:10px;font-size:7px;font-weight:700;color:var(--navy)}
.contact{position:absolute;font-size:5px;line-height:1.55;color:var(--muted)}
.card__contact{left:96px;top:30px}
.letterhead{left:437px;top:29px;width:326px;height:427px}
.letterhead__brand{position:absolute;left:20px;top:18px;width:80px}
.letterhead__contact{right:22px;top:16px;text-align:left;left:220px}
.letterhead__seal{position:absolute;left:50%;top:48%;width:120px;height:120px;border-radius:50%;background:var(--faint);transform:translate(-50%,-50%)}
.letterhead__band{position:absolute;left:0;right:0;bottom:0;height:8px;background:linear-gradient(90deg,var(--green),var(--teal),var(--navy))}
.envelope--back{left:792px;top:29px;width:384px;height:150px}
.envelope--mid{left:780px;top:125px;width:384px;height:150px}
.flap{position:absolute;left:0;top:0;width:100%;height:100%}
.envelope__seal{position:absolute;left:50%;top:68px;width:34px;height:34px;border-radius:50%;background:var(--navy);opacity:.8;transform:translateX(-50%)}
.envelope--front{left:667px;top:216px;width:427px;height:247px}
.envelope__brand{position:absolute;left:18px;top:92px;width:90px}
.envelope__contact{left:18px;top:178px}
.envelope__seal--front{top:20px;width:40px;height:40px;background:var(--paper);opacity:.9}
</style>
</head>
<body>

<!-- Business cards -->
<div class="card" style="left:24px;top:65px">
  <div class="card__brand brand brand--small"><span class="brand__dot"></span>Corvane Oral Care</div>
  <div class="card__name">R. Lucien Dorvash</div>
  <div class="contact card__contact">2483 W Perrin Ave.<br>Baytown, TX 77520<br>Phone: 281-555-0142<br>Fax: 281-555-0143<br>dentist@qbl.zx.com<br>www.corvaneoralcare.com</div>
</div>
<div class="card" style="left:228px;top:65px">
  <div class="card__brand brand brand--small"><span class="brand__dot"></span>Corvane Oral Care</div>
  <div class="card__name">R. Lucien Dorvash</div>
  <div class="contact card__contact">2483 W Perrin Ave.<br>Baytown, TX 77520<br>Phone: 281-555-0142<br>Fax: 281-555-0143<br>dentist@qbl.zx.com<br>www.corvaneoralcare.com</div>
</div>

<div class="card" style="left:24px;top:192px">
  <div class="brand brand--center"><span class="brand__dot"></span>Corvane Oral Care</div>
</div>
<div class="card" style="left:228px;top:192px">
  <div class="mark"></div>
</div>

<div class="card card--green" style="left:24px;top:317px">
  <div class="brand brand--center"><span class="brand__dot"></span>Corvane Oral Care</div>
</div>
<div class="card card--silver" style="left:228px;top:317px">
  <div class="mark" style="background:#1d1d1d"></div>
</div>

<!-- Letterhead -->
<div class="letterhead">
  <div class="letterhead__brand brand brand--small"><span class="brand__dot"></span>Corvane Oral Care</div>
  <div class="contact letterhead__contact">2483 W Perrin Ave.<br>Baytown, TX 77520<br>Phone: 281-555-0142<br>dentist@qbl.zx.com<br>www.corvaneoralcare.com</div>
  <div class="letterhead__seal"></div>
  <div class="letterhead__band"></div>
</div>

<!-- Envelopes, white -->
<div class="envelope envelope--back">
  <svg class="flap" viewBox="0 0 384 150" preserveAspectRatio="none"><path d="M0 0 L192 78 L384 0" fill="none" stroke="#d4d4d4" stroke-width="1.5"/></svg>
</div>
<div class="envelope envelope--mid">
  <svg class="flap" viewBox="0 0 384 150" preserveAspectRatio="none"><path d="M0 0 L192 78 L384 0" fill="none" stroke="#d4d4d4" stroke-width="1.5"/></svg>
  <div class="envelope__seal"></div>
</div>

<!-- Envelope, front with coloured flap -->
<div class="envelope envelope--front">
  <svg class="flap" viewBox="0 0 427 247" preserveAspectRatio="none">
    <defs>
      <linearGradient id="flapFill" x1="0" y1="0" x2="1" y2="0">
        <stop offset="0" stop-color="#8cc63f"/>
        <stop offset=".6" stop-color="#5fa8a0"/>
        <stop offset="1" stop-color="#2c4a8f"/>
      </linearGradient>
    </defs>
    <path d="M0 0 H427 V30 Q213 80 0 30 Z" fill="url(#flapFill)"/>
  </svg>
  <div class="envelope__seal envelope__seal--front"></div>
  <div class="envelope__brand brand brand--small"><span class="brand__dot"></span>Corvane Oral Care</div>
  <div class="contact envelope__contact">2483 W Perrin Ave.<br>Baytown, TX 77520<br>www.corvaneoralcare.com</div>
</div>

</body>
</html>
```